Business Card for Yachting Management Company

Need a business card design for a new yachting project management company. Attached is the logo for the company.
Our clients are large yacht owners and captains.
Design must be in the style of the logo. Modern, elegant.

Example of data to show:
Oliver Tennant
Project Manager
(+34) 612 870 334
oliver@quarvel.net
Quarvel Management - Marisol Tower, Office 22 - NDR - Palma de Mallorca

The data above will have to be changed (by me) for the different people in the company over the next years.

Will be printed using CardHarbor (Lustrel Business Cards). They provide these guidelines for the size:
"the actual size of the card is 1050 x 600 pixels. However, the full bleed size is 1083 x 633 pixels, and the safe printing area is 1008 x 558 pixels."

```html
<!DOCTYPE html>
<html lang="en">
<head>
<meta charset="utf-8">
<title>Quarvel Management – Business Card</title>
<link rel="stylesheet" href="https://fonts.googleapis.com/css2?family=Montserrat:wght@400;500;700&display=swap">
<style>
  :root {
    --brand-blue: #0a70bf;
    --ink: #1d1d1d;
    --rule: #2a2a2a;
    --paper: #ffffff;
    --backdrop: #d6d6d6;
  }
  * { box-sizing: border-box; margin: 0; padding: 0; }
  html, body { width: 1200px; height: 913px; overflow: hidden; }
  body {
    background: var(--backdrop);
    font-family: "Montserrat", sans-serif;
    color: var(--ink);
    display: flex;
    flex-direction: column;
    align-items: center;
    justify-content: center;
    gap: 40px;
  }
  .card {
    width: 640px;
    height: 366px;
    position: relative;
    box-shadow: 0 10px 28px rgba(0,0,0,0.25);
  }
  /* Front */
  .card--front {
    background: var(--paper);
    border: 2px solid var(--brand-blue);
  }
  .wordmark {
    color: var(--brand-blue);
    font-weight: 700;
    line-height: 1;
  }
  .card--front .wordmark {
    position: absolute;
    top: 52px;
    right: 120px;
    text-align: center;
  }
  .wordmark__name { display: block; font-size: 54px; letter-spacing: -1px; }
  .wordmark__sub { display: block; font-size: 17px; letter-spacing: 9px; margin-top: 10px; padding-left: 9px; }
  .holder {
    position: absolute;
    left: 44px;
    top: 160px;
  }
  .holder__name {
    color: var(--brand-blue);
    font-weight: 700;
    font-size: 27px;
  }
  .holder__title { font-size: 15px; margin-top: 4px; }
  .divider {
    position: absolute;
    left: 44px;
    right: 40px;
    top: 228px;
    border-top: 1.5px solid var(--rule);
  }
  .contacts {
    position: absolute;
    left: 44px;
    top: 244px;
    list-style: none;
    font-size: 15px;
    line-height: 1.55;
  }
  .contacts li { display: flex; align-items: center; gap: 10px; }
  .contacts svg { width: 13px; height: 13px; flex: none; fill: var(--brand-blue); }
  .address {
    position: absolute;
    left: 290px;
    top: 244px;
    font-size: 15px;
    line-height: 1.55;
    font-style: normal;
  }
  /* Back */
  .card--back {
    background: var(--brand-blue);
    display: flex;
    align-items: center;
    justify-content: center;
  }
  .card--back .wordmark { color: var(--paper); text-align: center; }
  .card--back .wordmark__name { font-size: 92px; letter-spacing: -2px; }
  .card--back .wordmark__sub { font-size: 26px; letter-spacing: 14px; padding-left: 14px; margin-top: 14px; }
</style>
</head>
<body>
  <section class="card card--front" aria-label="Business card front">
    <div class="wordmark">
      <span class="wordmark__name">Quarvel</span>
      <span class="wordmark__sub">MANAGEMENT</span>
    </div>
    <div class="holder">
      <h1 class="holder__name">Oliver Tennant</h1>
      <p class="holder__title">Project Manager</p>
    </div>
    <div class="divider"></div>
    <ul class="contacts">
      <li>
        <svg viewBox="0 0 16 16" aria-hidden="true"><path d="M3.6 1.2l2.3 2.6-1.3 1.7c.9 2 2.5 3.6 4.5 4.5l1.7-1.3 2.6 2.3-1.5 2.3C6.8 13.3 2.7 9.2 1.3 3.1z"/></svg>
        (+34) 612 870 334
      </li>
      <li>
        <svg viewBox="0 0 16 16" aria-hidden="true"><path d="M1 3h14v10H1z M1.8 3.8L8 9l6.2-5.2" fill="var(--brand-blue)" stroke="#fff" stroke-width="1"/></svg>
        oliver@quarvel.net
      </li>
      <li>
        <svg viewBox="0 0 16 16" aria-hidden="true"><circle cx="8" cy="8" r="7"/><path d="M1 8h14M8 1c-3 3.5-3 10.5 0 14M8 1c3 3.5 3 10.5 0 14" fill="none" stroke="#fff" stroke-width="1"/></svg>
        Your webadress here
      </li>
    </ul>
    <address class="address">
      Quarvel Management - Marisol Tower,<br>
      Office 22 - NDR - Palma de Mallorca
    </address>
  </section>

  <section class="card card--back" aria-label="Business card back">
    <div class="wordmark">
      <span class="wordmark__name">Quarvel</span>
      <span class="wordmark__sub">MANAGEMENT</span>
    </div>
  </section>
</body>
</html>
```